Redesign of an insurance website

Attached is an insurance website that I need to redesign. Currently the website is too dark. I like for example www.brenvalo.com . Could you make the website lighter and change the structure a little so that it is more user friendly?

Industry/Entity Type

Insurance

Number of Pages Required

4 page

```html
<!DOCTYPE html>
<html lang="en">
<head>
<meta charset="utf-8">
<title>Insurance Company</title>
<link rel="stylesheet" href="https://fonts.googleapis.com/css2?family=Raleway:wght@400;500;600;700&display=swap">
<style>
:root{
  --navy:#12356b;
  --blue:#1f4fa8;
  --teal:#3bbfcf;
  --teal-dark:#2a9aa8;
  --green:#86e38e;
  --yellow:#fde04a;
  --orange:#ff8a3c;
  --ink:#333333;
  --muted:#8a8a8a;
  --line:#e6e6e6;
  --card:#f4f4f4;
  --white:#ffffff;
}
*{box-sizing:border-box;margin:0;padding:0}
html,body{width:1200px;height:2812px;overflow:hidden}
body{position:relative;background:var(--white);font-family:"Raleway",Arial,sans-serif;color:var(--ink)}
.abs{position:absolute}
.topline{left:0;top:0;width:1200px;height:5px;background:var(--blue)}
.brand{left:86px;top:28px;font-weight:700;font-size:34px;letter-spacing:2px;color:var(--blue)}
.utility{right:86px;top:20px;display:flex;gap:16px}
.nav{top:54px;font-size:14px;font-weight:500;letter-spacing:.5px;color:#222}
.nav-sep{top:54px;font-size:14px;color:#999}
.hero{left:0;top:88px;width:1200px;height:602px;background:linear-gradient(135deg,#d9cfc9 0%,#eae3df 40%,#f3d6d6 60%,#d6cdc8 100%)}
.hero-title{left:0;top:338px;width:1200px;text-align:center;font-size:40px;font-weight:400;letter-spacing:1px;color:#2a2a2a}
.zip{left:274px;top:422px;width:429px;height:58px;background:rgba(255,255,255,.55);color:#555;font-size:18px;padding:0 28px;line-height:58px}
.btn-quote{left:714px;top:422px;width:212px;height:58px;background:var(--blue);color:var(--white);font-size:18px;text-align:center;line-height:58px;font-weight:500}
.service-circle{width:150px;height:150px;border-radius:50%;border:3px solid var(--white);display:flex;align-items:center;justify-content:center;top:643px}
.service-label{top:807px;width:260px;text-align:center;font-size:20px;color:#333}
.vdiv{top:740px;width:1px;height:122px;background:var(--line)}
.hdiv{left:86px;top:879px;width:1034px;height:1px;background:var(--line)}
.about-frame{left:113px;top:1022px;width:465px;height:328px;border:1px solid #ececec}
.about-photo{left:88px;top:996px;width:469px;height:333px;background:linear-gradient(135deg,#eef1f3 0%,#c9d3db 50%,#5aa9c3 100%)}
.eyebrow{left:608px;top:996px;font-size:18px;color:#555;letter-spacing:.5px}
.about-title{left:608px;top:1030px;font-size:34px;font-weight:500;color:#222;letter-spacing:.5px}
.about-rule{left:608px;top:1080px;width:65px;height:2px;background:var(--blue)}
.about-text{left:608px;width:508px;font-size:13.5px;line-height:21px;color:#777;text-align:justify}
.btn-primary{background:var(--blue);color:var(--white);font-size:13px;text-align:center;font-weight:500}
.band{left:0;top:1513px;width:1200px;height:184px;background:var(--teal)}
.avatar{left:534px;top:1443px;width:132px;height:132px;border-radius:50%;border:4px solid var(--white);background:radial-gradient(circle at 50% 45%,#e9d6c6 0%,#c8b39e 55%,#9fb8c8 100%);box-shadow:0 0 0 1px #ddd}
.quote{left:120px;top:1597px;width:960px;text-align:center;color:var(--white);font-size:14px;line-height:22px}
.quote-name{left:0;top:1652px;width:1200px;text-align:center;font-size:13px;color:var(--white);font-weight:500}
.quote-name em{color:#bff0f5;font-weight:400}
.card{top:1792px;width:323px;height:375px;background:var(--card)}
.card-icon{position:absolute;left:110px;top:42px;width:104px;height:104px;border-radius:50%;display:flex;align-items:center;justify-content:center}
.card-title{position:absolute;left:0;top:172px;width:100%;text-align:center;font-size:22px;font-weight:500;color:#222;letter-spacing:.5px}
.card-text{position:absolute;left:30px;top:212px;width:263px;text-align:center;font-size:13px;line-height:21px;color:#8a8a8a}
.card-btn{position:absolute;left:100px;top:306px;width:124px;height:36px;background:#e3e3e3;font-size:13px;line-height:36px;text-align:center;color:#333;font-weight:500}
.footer{left:0;top:2434px;width:1200px;height:378px;background:var(--navy)}
.contact{left:200px;top:2278px;width:798px;height:304px;background:var(--teal);border:3px solid var(--white)}
.contact-title{position:absolute;left:0;top:30px;width:100%;text-align:center;color:var(--white);font-size:32px;letter-spacing:1px}
.contact-title::before,.contact-title::after{content:"";display:inline-block;width:40px;height:1px;background:var(--white);vertical-align:middle;margin:0 16px}
.field{position:absolute;border-bottom:1px solid rgba(255,255,255,.75);color:var(--white);font-size:12px;padding-bottom:8px}
.submit{position:absolute;left:334px;top:226px;width:128px;height:39px;background:var(--teal-dark);color:var(--white);text-align:center;line-height:39px;font-size:13px}
.footer-brand{left:0;top:2618px;width:1200px;text-align:center;font-weight:700;font-size:26px;letter-spacing:2px;color:#2f8fd6}
.footer-links{left:0;top:2676px;width:1200px;display:flex;justify-content:center;gap:22px;font-size:12px;color:var(--white);font-weight:500}
.footer-links span.sep{color:#6d86ad}
.social{left:0;top:2719px;width:1200px;display:flex;justify-content:center;gap:28px}
.social span{width:22px;height:22px;border-radius:50%;background:#5f7597}
.footer-rule{left:0;top:2770px;width:1200px;height:1px;background:#2a4a7e}
.copyright{left:0;top:2782px;width:1200px;text-align:center;font-size:12px;color:#aab7cc}
</style>
</head>
<body>
<div class="abs topline"></div>
<header>
  <div class="abs brand">INSURANCE COMPANY</div>
  <div class="abs utility">
    <svg width="18" height="18" viewBox="0 0 18 18"><circle cx="9" cy="9" r="8" fill="var(--blue)"/><path d="M4 9h10" stroke="#fff" stroke-width="2"/></svg>
    <svg width="14" height="18" viewBox="0 0 14 18"><path d="M7 1a6 6 0 0 0-6 6c0 4.5 6 10 6 10s6-5.5 6-10a6 6 0 0 0-6-6z" fill="var(--blue)"/><circle cx="7" cy="7" r="2.2" fill="#fff"/></svg>
  </div>
  <nav>
    <div class="abs nav" style="left:722px">INSURANCE</div>
    <div class="abs nav-sep" style="left:832px">|</div>
    <div class="abs nav" style="left:869px">INFORMATION</div>
    <div class="abs nav-sep" style="left:992px">|</div>
    <div class="abs nav" style="left:1029px">YOUR POLICY</div>
  </nav>
</header>

<section>
  <div class="abs hero" role="img" aria-label="Hand dropping a coin into a pink piggy bank"></div>
  <h1 class="abs hero-title">MORE THAN JUST CAR INSURANCE</h1>
  <div class="abs zip">Enter Your Zip...</div>
  <div class="abs btn-quote">START QUOTE</div>
</section>

<section>
  <div class="abs service-circle" style="left:131px;background:var(--green)">
    <svg width="64" height="44" viewBox="0 0 64 44"><path d="M8 22l6-14c1-3 3-4 6-4h24c3 0 5 1 6 4l6 14h2v14h-6v6h-8v-6H20v6h-8v-6H6V22z" fill="#fff"/><rect x="16" y="10" width="32" height="11" rx="2" fill="var(--green)"/><circle cx="15" cy="28" r="3.5" fill="var(--green)"/><circle cx="49" cy="28" r="3.5" fill="var(--green)"/></svg>
  </div>
  <div class="abs service-label" style="left:76px">CAR INSURANCE</div>
  <div class="abs vdiv" style="left:332px"></div>

  <div class="abs service-circle" style="left:394px;background:var(--yellow)">
    <svg width="60" height="56" viewBox="0 0 60 56"><path d="M30 4L4 28h8v24h14V38h8v14h14V28h8z" fill="#fff"/></svg>
  </div>
  <div class="abs service-label" style="left:339px">HOME INSURANCE</div>
  <div class="abs vdiv" style="left:596px"></div>

  <div class="abs service-circle" style="left:656px;background:var(--orange)">
    <svg width="64" height="40" viewBox="0 0 64 40"><path d="M4 26l6-2 6 5 40-16c4-1 6 2 2 4L30 30l-16 6-8-2z" fill="#fff"/><path d="M22 18L14 6h6l16 8z" fill="#fff"/><path d="M28 30l8 8h6l-4-12z" fill="#fff"/></svg>
  </div>
  <div class="abs service-label" style="left:601px">TRAVEL INSURANCE</div>
  <div class="abs vdiv" style="left:862px"></div>

  <div class="abs service-circle" style="left:921px;background:var(--teal)">
    <svg width="60" height="60" viewBox="0 0 60 60"><g fill="#fff"><rect x="4" y="34" width="14" height="8" transform="rotate(-45 11 38)"/><rect x="40" y="16" width="14" height="8" transform="rotate(-45 47 20)"/><path d="M16 36l14-14 8 2 6 6-16 16c-2 2-4 2-6 0z"/><path d="M24 22l8-6 6 4-6 4z"/></g></svg>
  </div>
  <div class="abs service-label" style="left:866px">BUSINESS INSURANCE</div>
  <div class="abs hdiv"></div>
</section>

<section>
  <div class="abs about-frame"></div>
  <div class="abs about-photo" role="img" aria-label="Two people reviewing and signing an insurance document at a desk"></div>
  <div class="abs eyebrow">WHO WE ARE</div>
  <h2 class="abs about-title">ABOUT INSURANCE AGENCY</h2>
  <div class="abs about-rule"></div>
  <p class="abs about-text" style="top:1110px">Lorem ipsum dolor sit amet, consectetur adipiscing elit. Aliquam vehicula mollis urna vel dignissim. Integer tincidunt viverra est, non congue.</p>
  <p class="abs about-text" style="top:1172px">Lorem ipsum dolor sit amet, consectetur adipiscing elit. Aliquam vehicula mollis urna vel dignissim. Integer tincidunt viverra est, non congue lorem tempor ac. Sed dolor velit, convallis quis erat in, molestie eleifend enim. Integer eu metus at orci scelerisque rutrum. Vivamus condimentum, ipsum vitae iaculis cursus, turpis nisl ultricies massa, sit amet ultrices nunc dui at tellus.</p>
  <div class="abs btn-primary" style="left:615px;top:1311px;width:156px;height:41px;line-height:41px">LEARN MORE</div>
</section>

<section>
  <div class="abs band"></div>
  <div class="abs avatar" role="img" aria-label="Portrait of a client"></div>
  <p class="abs quote">An entity which provides insurance is known as an insurer, insurance company, or insurance carrier. A person or entity who buys insurance is known as an insured or policyholder. The action involves a contract.</p>
  <div class="abs quote-name">DANA WHITLOW, <em>Assistant</em></div>
</section>

<section>
  <div class="abs card" style="left:88px">
    <div class="card-icon" style="background:var(--orange)"><svg width="44" height="52" viewBox="0 0 44 52"><rect x="10" y="2" width="24" height="44" rx="4" fill="#fff"/><rect x="14" y="8" width="16" height="30" fill="var(--orange)"/><path d="M4 30c0-6 6-8 8-4v16H8c-2 0-4-2-4-4z" fill="#fff"/></svg></div>
    <div class="card-title">INSAURANCE MOBILE</div>
    <p class="card-text">Nunc posuere ornare massa quis convallis. Nunc at pharetra metus, sed feugiat lorem. Sed fringilla.</p>
    <div class="card-btn">LEARN MORE</div>
  </div>
  <div class="abs card" style="left:439px">
    <div class="card-icon" style="background:var(--green)"><svg width="44" height="52" viewBox="0 0 44 52"><path d="M8 2h20l10 10v34H8z" fill="#fff"/><g stroke="var(--green)" stroke-width="3"><path d="M14 18h16M14 25h16M14 32h10"/></g><circle cx="34" cy="40" r="8" fill="#fff" stroke="var(--green)" stroke-width="2"/><path d="M34 36v5" stroke="var(--green)" stroke-width="2.5"/><circle cx="34" cy="44" r="1.3" fill="var(--green)"/></svg></div>
    <div class="card-title">CLAIMS CENTER</div>
    <p class="card-text">Nunc posuere ornare massa quis convallis. Nunc at pharetra metus, sed feugiat lorem. Sed fringilla.</p>
    <div class="card-btn">LEARN MORE</div>
  </div>
  <div class="abs card" style="left:789px">
    <div class="card-icon" style="background:var(--yellow)"><svg width="40" height="48" viewBox="0 0 40 48"><path d="M10 20v-8a10 10 0 0 1 20 0" fill="none" stroke="#fff" stroke-width="4"/><rect x="4" y="20" width="32" height="24" rx="3" fill="#fff"/><rect x="18" y="28" width="4" height="8" fill="var(--yellow)"/></svg></div>
    <div class="card-title">NO LOGIN REQUIRED</div>
    <p class="card-text">Nunc posuere ornare massa quis convallis. Nunc at pharetra metus, sed feugiat lorem. Sed fringilla.</p>
    <div class="card-btn">LEARN MORE</div>
  </div>
</section>

<footer>
  <div class="abs footer"></div>
  <div class="abs contact">
    <h2 class="contact-title">CONTACT US</h2>
    <div class="field" style="left:50px;top:103px;width:320px">Name.</div>
    <div class="field" style="left:428px;top:103px;width:321px">Phone No.</div>
    <div class="field" style="left:50px;top:172px;width:699px">Massage.</div>
    <div class="submit">SUBMIT</div>
  </div>
  <div class="abs footer-brand">INSURANCE COMPANY</div>
  <div class="abs footer-links">
    <span>PRIVACY</span><span class="sep">|</span><span>LEGAL &amp; SECURITY</span><span class="sep">|</span><span>CAREERS</span><span class="sep">|</span><span>CONTACT US</span><span class="sep">|</span><span>SITE MAP</span>
  </div>
  <div class="abs social"><span></span><span></span><span></span></div>
  <div class="abs footer-rule"></div>
  <div class="abs copyright">copyright @ 2017 insurance company</div>
</footer>
</body>
</html>
```